Calvin Pruett Insurance Biz Card
Biz card and stationary
Calvin Pruett Insurance Biz Card - Financial Services
Creative Brief
Professional
Calvin Pruett
Independent Agent
Ashford Hills, NC
pruettgroup@lanvex.example.net
www.calvinpruettinsurance.example.com
please use the logo we upload, and keep all font at a size 9 or 10.
please use the content we upload for an example of the back of the card

```html
<!DOCTYPE html>
<html lang="en">
<head>
<meta charset="utf-8">
<title>Calvin Pruett Insurance – Business Card</title>
<link href="https://fonts.googleapis.com/css2?family=Crimson+Pro:wght@400;600;700&display=swap" rel="stylesheet">
<style>
  :root {
    --navy: #1d3468;
    --grey: #9a9892;
    --ink: #1f1f24;
    --paper: #ffffff;
    --backdrop: #ecebe8;
  }
  * { margin: 0; padding: 0; box-sizing: border-box; }
  html, body {
    width: 1200px;
    height: 778px;
    overflow: hidden;
    background: var(--backdrop);
    font-family: "Crimson Pro", "Times New Roman", serif;
  }
  .card {
    position: absolute;
    left: 60px;
    top: 79px;
    width: 1080px;
    height: 620px;
    background: var(--paper);
    border: 1px solid #dcdad5;
  }
  .brand {
    position: absolute;
    left: 81px;
    top: 62px;
    display: flex;
    align-items: center;
    gap: 22px;
  }
  .brand-square {
    width: 120px;
    height: 120px;
    background: var(--navy);
  }
  .brand-name {
    color: var(--navy);
    font-weight: 600;
    font-size: 50px;
    line-height: 1.0;
    letter-spacing: -0.5px;
  }
  .agent {
    position: absolute;
    right: 90px;
    top: 240px;
    text-align: right;
  }
  .agent-name {
    color: var(--navy);
    font-weight: 700;
    font-size: 42px;
    line-height: 1.1;
    letter-spacing: -0.5px;
  }
  .agent-title {
    color: var(--grey);
    font-weight: 600;
    font-size: 32px;
    line-height: 1.2;
  }
  .side-tab {
    position: absolute;
    left: 0;
    top: 375px;
    width: 30px;
    height: 162px;
    background: var(--navy);
    border-radius: 0 18px 18px 0;
  }
  .location {
    position: absolute;
    left: 81px;
    top: 366px;
    color: var(--ink);
    font-size: 32px;
  }
  .contact-list {
    position: absolute;
    left: 81px;
    top: 442px;
    list-style: none;
  }
  .contact-list li {
    display: flex;
    align-items: center;
    gap: 12px;
    height: 34px;
    color: var(--ink);
    font-size: 30px;
  }
  .contact-list svg {
    width: 16px;
    height: 16px;
    fill: var(--navy);
    flex: none;
  }
</style>
</head>
<body>
  <main class="card">
    <div class="brand">
      <div class="brand-square"></div>
      <div class="brand-name">Calvin Pruett<br>Insurance, LLC</div>
    </div>

    <div class="agent">
      <div class="agent-name">Calvin Pruett</div>
      <div class="agent-title">Independent Agent</div>
    </div>

    <div class="side-tab"></div>

    <div class="location">Ashford Hills, NC</div>

    <ul class="contact-list">
      <li>
        <svg viewBox="0 0 16 16" aria-hidden="true"><path d="M3.5 1.5 6 1l1.5 3.5-2 1.3a8 8 0 0 0 4.7 4.7l1.3-2L15 10l-.5 2.5c-.2.9-1 1.5-1.9 1.4C6.6 13.3 2.7 9.4 2.1 3.4c-.1-.9.5-1.7 1.4-1.9Z"/></svg>
        336-555-0148
      </li>
      <li>
        <svg viewBox="0 0 16 16" aria-hidden="true"><path d="M1 3h14v10H1V3Zm1.6 1.2L8 8.4l5.4-4.2H2.6ZM2.2 5.3v6.5h11.6V5.3L8 9.8 2.2 5.3Z"/></svg>
        pruettgroup@lanvex.example.net
      </li>
      <li>
        <svg viewBox="0 0 16 16" aria-hidden="true"><circle cx="8" cy="8" r="7"/><path d="M5 6.5 7 5l3 .5 1 2-2 1.5.5 2.5-2 1-1-2.5-2-1 .5-2.5Z" fill="#ffffff"/></svg>
        www.calvinpruettinsurance.example.com
      </li>
    </ul>
  </main>
</body>
</html>
```